DL Flyer for conservation/restoration business

I am an objects conservator and run a business called FormKeep Conservation. I specialise in conserving and restoring 3 dimensional artworks and artefacts in Perth, Western Australia. I dont work on paintings, paper or textiles but pretty much everything else such as sculptures, metal, wood, ceramics etc. So far I have been reasonably successful in marketing to small museums and councils. However, I would like to pick up some more work from private individuals living in the more affluent areas of Perth.

I would like to have a DL flyer designed to do a letterbox drop in my target areas. I would like something professional and eyecatching that wont get thrown away. Also it will make the business look trustworthy.

I would like to have something that will go with my existing logo if possible.

Target Market(s)

wealthy individuals over 50 who enjoy collecting art / antiques

Industry/Entity Type

Marketing

Requirements
Must have
• I would like a good background image or images of suitable artworks/ artefacts/ conservator at work (hands only). Also include my logo as the business name.

I am happy to take advice on advertising, but my preference is for the text in the attached word file (order can be rearranged):

I would like to be able to edit the flyer if necessary at a later date, and would like it to be compatible with MS Publisher.
Should not have
• Do not include any images of paintings, textiles, paper or books.

```html
<!DOCTYPE html>
<html lang="en">
<head>
<meta charset="utf-8">
<title>FormKeep Conservation – DL Flyer</title>
<link rel="stylesheet" href="https://fonts.googleapis.com/css2?family=Poppins:wght@300;400;600;700&display=swap">
<style>
  :root {
    --page-bg: #ececec;
    --paper: #ffffff;
    --charcoal: #404445;
    --ink: #111111;
    --brand-red: #b3202b;
    --accent-cyan: #4cc6ee;
    --text-light: #ffffff;
  }
  * { margin: 0; padding: 0; box-sizing: border-box; }
  html, body {
    width: 897px; height: 1200px; overflow: hidden;
    background: var(--page-bg);
    font-family: "Poppins", Arial, sans-serif;
  }
  .flyer-stage {
    position: absolute; left: 177px; top: 18px;
    width: 543px; height: 1164px; overflow: hidden;
  }
  .flyer {
    position: absolute; left: 0; top: 0;
    width: 452px; height: 970px;
    transform: scale(1.2); transform-origin: 0 0;
    background: var(--paper);
    overflow: hidden;
  }
  .flyer-art { position: absolute; inset: 0; width: 452px; height: 970px; }

  .brand {
    position: absolute; top: 44px; left: 136px;
    display: flex; align-items: center; gap: 14px;
  }
  .brand-dot {
    width: 60px; height: 60px; border-radius: 50%;
    background: var(--brand-red);
  }
  .brand-name {
    font-weight: 600; color: var(--brand-red);
    font-size: 28px; line-height: 1.0;
  }
  .brand-name small { display: block; font-size: 15px; letter-spacing: 3.5px; margin-top: 2px; }

  .headline {
    position: absolute; top: 226px; left: 20px; width: 406px;
    font-weight: 700; font-size: 57px; line-height: 54px;
    color: var(--text-light);
    -webkit-text-stroke: 2.4px var(--ink);
    paint-order: stroke fill;
    letter-spacing: -0.5px;
    white-space: nowrap;
  }
  .headline span { display: block; }
  .headline .line-1, .headline .line-3 { text-align: left; }
  .headline .line-2, .headline .line-4 { text-align: right; }

  .services {
    position: absolute; top: 598px; left: 28px; width: 416px;
    color: var(--text-light);
  }
  .services-title { font-weight: 700; font-size: 19px; line-height: 25px; }
  .services-title span { display: block; padding-left: 4px; }
  .service-list {
    list-style: none; margin-top: 4px;
    color: var(--accent-cyan); font-weight: 400;
    font-size: 15px; line-height: 24px;
  }
  .service-list li {
    position: relative; padding-left: 11px; margin-left: -5px; margin-bottom: 4px;
    white-space: nowrap;
  }
  .service-list li::before { content: "•"; position: absolute; left: 0; }

  .credentials {
    position: absolute; top: 770px; left: 0; width: 452px;
    text-align: center; color: var(--text-light);
    font-size: 14px; line-height: 22px;
  }

  .contact {
    position: absolute; top: 854px; left: 0; width: 452px;
    text-align: center; color: var(--text-light);
    white-space: nowrap;
  }
  .contact-name { color: var(--accent-cyan); font-weight: 700; font-size: 15px; line-height: 22px; }
  .contact-phone { font-weight: 700; font-size: 24px; line-height: 28px; }
  .contact-email { font-size: 14px; line-height: 18px; }
  .contact-web { color: var(--accent-cyan); font-weight: 700; font-size: 24px; line-height: 32px; letter-spacing: -0.2px; }
</style>
</head>
<body>
  <div class="flyer-stage">
    <div class="flyer">
      <svg class="flyer-art" viewBox="0 0 452 970" xmlns="http://www.w3.org/2000/svg">
        <defs>
          <radialGradient id="ceramicsGlow" cx="0.4" cy="0.45" r="0.75">
            <stop offset="0" stop-color="#6f83d6"/>
            <stop offset="0.45" stop-color="#3a4fae"/>
            <stop offset="0.8" stop-color="#b79a86"/>
            <stop offset="1" stop-color="#d98a3c"/>
          </radialGradient>
        </defs>
        <path role="img" aria-label="Photograph of hand-painted blue enamel vases and ceramic pieces"
              d="M0,118 Q230,80 452,250 L452,620 Q150,585 0,430 Z" fill="url(#ceramicsGlow)"/>
        <path d="M0,430 Q150,585 452,620 L452,970 L0,970 Z" fill="var(--charcoal)"/>
        <path d="M0,430 Q150,585 452,620 L452,632 Q150,598 0,444 Z" fill="var(--ink)"/>
      </svg>

      <div class="brand">
        <div class="brand-dot"></div>
        <div class="brand-name">FormKeep<small>conservation</small></div>
      </div>

      <h1 class="headline">
        <span class="line-1">Perth’s</span>
        <span class="line-2">most trusted</span>
        <span class="line-3">conservation</span>
        <span class="line-4">service</span>
      </h1>

      <section class="services">
        <h2 class="services-title">Conservation and<span>restoration of objects including:</span></h2>
        <ul class="service-list">
          <li>Historical items, antiques, ceramics and sculpture</li>
          <li>Custom made display fittings and supports.</li>
          <li>Free advice on storage and display techniques<br>to help preserve your treasured items.</li>
        </ul>
      </section>

      <p class="credentials">
        University trained conservator with over 20 years’<br>
        experience in major galleries and museums.<br>
        Offering free quotes in your area on:
      </p>

      <div class="contact">
        <p class="contact-name">Helen Marlowe</p>
        <p class="contact-phone">5550 4821 / 0491 570 156</p>
        <p class="contact-email">studio@formkeepconservation.com</p>
        <p class="contact-web">www.formkeepconservation.com</p>
      </div>
    </div>
  </div>
</body>
</html>
```